Tulvos Vending Machine sucht Design.
Aufgabenstellung
Designvorgabe für Tulvo's Vending Machine
Übersicht:
Wir haben einen Verkaufsautomaten an einem bestimmten Ort. Der Automat bietet Snacks, Getränke aus aller Welt (sowie Standardoptionen) und E-Zigaretten. Ich möchte den Verkaufsautomaten personalisieren und eine unverwechselbare visuelle Identität schaffen. Beim Aufstellen eines anderen Verkaufsautomaten möchte ich, dass dieser sofort erkennbar ist. Der Name des Verkaufsautomaten ist „Tulvo's“ (derzeit gibt es kein Logo), und ich bin offen für kreative Designs, die sowohl Text als auch visuelle Grafiken zu den genannten Produktkategorien kombinieren. Abmessungen und ein Bild sind beigefügt.
Schlüsselelemente:
Snacks und Getränke aus verschiedenen Ländern, auch Standardoptionen.
E-Zigaretten.
Designanforderungen:
Name: Tulvo's
Logo: Derzeit keines; offen für kreative Vorschläge.
Stil: Kreieren Sie ein einzigartiges und auffälliges Design, das die internationale Vielfalt an Snacks und Getränken sowie die Einbeziehung von E-Zigaretten widerspiegelt.
Wiedererkennung: Stellen Sie sicher, dass das Design einprägsam und auch auf den ersten Blick leicht erkennbar ist.
Abmessungen: Outdoormaße (B x H x T) 1030 x 1900 x 1010 mm
Experimentieren Sie ruhig mit Farben, Schriftarten und grafischen Elementen.
Erwägen Sie die Integration von Symbolen oder Icons, die Snacks, Getränke und E-Zigaretten darstellen, um das Produktsortiment visuell zu kommunizieren.
Um die Konsistenz zu gewährleisten, sollte das Design an zukünftige Verkaufsautomaten anpassbar sein.
Beigefügt:
Bild des Verkaufsautomaten.
Vielen Dank für Ihren kreativen Beitrag und ich freue mich darauf, die Designs für Tulvos Verkaufsautomaten zu sehen!

```html
<!DOCTYPE html>
<html lang="de">
<head>
<meta charset="utf-8">
<title>Tulvo's – Automatenfolierung</title>
<link rel="stylesheet" href="https://fonts.googleapis.com/css2?family=Fredoka:wght@600&family=Roboto:wght@400&display=swap">
<style>
  :root {
    --blush: #f6c5dc;
    --blush-light: #f9d6e6;
    --magenta: #dd2e87;
    --magenta-deep: #c9257a;
    --plum: #a3377f;
    --lilac: #c58bb4;
    --ink-purple: #55176b;
    --machine-black: #111114;
    --steel: #6d6d72;
    --dim-grey: #666666;
    --paper: #ffffff;
  }
  html, body {
    margin: 0;
    padding: 0;
    width: 1200px;
    height: 1200px;
    overflow: hidden;
    background: var(--paper);
  }
  .sheet {
    position: relative;
    width: 1200px;
    height: 1200px;
  }
  .panel {
    position: absolute;
    display: block;
  }
  .panel--left  { left: 129px; top: 271px; width: 314px; height: 590px; }
  .panel--front { left: 477px; top: 274px; width: 317px; height: 585px; }
  .panel--right { left: 828px; top: 271px; width: 314px; height: 590px; }

  .brand-name {
    font-family: 'Fredoka', sans-serif;
    font-weight: 600;
    fill: var(--magenta);
  }
  .brand-name--on-magenta {
    fill: var(--paper);
  }
  .tagline {
    font-family: 'Fredoka', sans-serif;
    font-weight: 600;
    fill: var(--ink-purple);
    stroke: var(--paper);
    stroke-width: 5px;
    paint-order: stroke;
  }
  .push-label {
    font-family: 'Roboto', sans-serif;
    font-size: 34px;
    letter-spacing: 6px;
    fill: #2a2a2e;
  }
  .sign-text {
    font-family: 'Roboto', sans-serif;
    fill: #ffffff;
  }

  .dimension {
    position: absolute;
    display: block;
  }
  .dimension-label {
    position: absolute;
    font-family: 'Roboto', sans-serif;
    font-size: 25px;
    color: var(--dim-grey);
    text-align: center;
    line-height: 1;
    white-space: nowrap;
  }
  .dimension-label--height {
    left: 78px;
    top: 566px;
    transform: translate(-50%, -50%) rotate(-90deg);
  }
  .dimension-label--left  { left: 129px; width: 314px; top: 908px; }
  .dimension-label--front { left: 477px; width: 317px; top: 908px; }
  .dimension-label--right { left: 828px; width: 314px; top: 908px; }
</style>
</head>
<body>
<main class="sheet">

  <!-- Side wall, left -->
  <svg class="panel panel--left" viewBox="0 0 503 945" preserveAspectRatio="none">
    <defs>
      <linearGradient id="sideTopBlob" x1="0" y1="0" x2="1" y2="1">
        <stop offset="0" stop-color="#e0338a"/>
        <stop offset="1" stop-color="#f08cbc"/>
      </linearGradient>
      <linearGradient id="sideCornerBlob" x1="0" y1="0" x2="1" y2="1">
        <stop offset="0" stop-color="#a6417f"/>
        <stop offset="1" stop-color="#d8a6c8"/>
      </linearGradient>
      <linearGradient id="sideCenterBlob" x1="0" y1="0" x2="0" y2="1">
        <stop offset="0" stop-color="#e86aa8"/>
        <stop offset="1" stop-color="#dd2e87"/>
      </linearGradient>
      <linearGradient id="productArt" x1="0" y1="0" x2="1" y2="1">
        <stop offset="0" stop-color="#f3b2d0"/>
        <stop offset="1" stop-color="#e985b6"/>
      </linearGradient>
    </defs>
    <rect class="panel-bg" width="503" height="945" fill="var(--blush)"/>
    <path class="blob blob--top" d="M0 0 H330 C250 20 230 60 215 120 C200 190 150 200 90 195 C40 190 15 185 0 185 Z" fill="url(#sideTopBlob)"/>
    <path class="blob blob--corner" d="M300 0 H503 V180 C470 200 420 210 380 190 C330 160 340 110 300 80 C280 60 280 20 300 0 Z" fill="url(#sideCornerBlob)"/>
    <path class="blob blob--tagline" d="M40 340 C70 300 160 320 230 325 C320 330 360 300 420 320 C480 340 490 420 470 470 C450 520 400 500 340 505 C310 508 320 535 290 535 C260 535 260 505 220 505 C150 505 60 510 35 450 C20 410 25 370 40 340 Z" fill="url(#sideCenterBlob)"/>
    <path class="band band--floor" d="M0 740 C120 720 200 760 300 745 C380 732 440 700 503 720 V890 H0 Z" fill="var(--plum)"/>
    <rect class="band band--base" y="888" width="503" height="57" fill="var(--magenta)"/>
    <text class="brand-name" x="250" y="300" font-size="128" text-anchor="middle">Tulvo's</text>
    <text class="tagline" x="262" y="405" font-size="46" text-anchor="middle">Snacks, Getränke</text>
    <text class="tagline" x="272" y="452" font-size="46" text-anchor="middle">und Vapes</text>
    <rect class="product-illustration" x="70" y="555" width="340" height="325" rx="22" fill="url(#productArt)" role="img" aria-label="Illustration: Getränkeflaschen, Chipstüte, Dose, Cracker, Energieriegel, Milchpackung und Keks in Pinktönen"/>
  </svg>

  <!-- Front door -->
  <svg class="panel panel--front" viewBox="0 0 507 936" preserveAspectRatio="none">
    <defs>
      <linearGradient id="frontTopBlob" x1="0" y1="0" x2="1" y2="1">
        <stop offset="0" stop-color="#e0338a"/>
        <stop offset="1" stop-color="#f08cbc"/>
      </linearGradient>
      <linearGradient id="frontCornerBlob" x1="0" y1="0" x2="1" y2="1">
        <stop offset="0" stop-color="#a6417f"/>
        <stop offset="1" stop-color="#d8a6c8"/>
      </linearGradient>
      <linearGradient id="frontBase" x1="0" y1="0" x2="0" y2="1">
        <stop offset="0" stop-color="#e75aa0"/>
        <stop offset="1" stop-color="#dd2e87"/>
      </linearGradient>
      <linearGradient id="productWindow" x1="0" y1="0" x2="0" y2="1">
        <stop offset="0" stop-color="#1c1b20"/>
        <stop offset="1" stop-color="#0c0c0e"/>
      </linearGradient>
    </defs>
    <rect class="panel-bg" width="507" height="936" fill="var(--blush)"/>
    <path class="blob blob--top" d="M0 0 H250 C230 60 180 70 120 80 C60 90 20 110 0 120 Z" fill="url(#frontTopBlob)"/>
    <path class="blob blob--corner" d="M330 0 H507 V500 C470 480 450 420 440 360 C420 240 380 140 350 80 C335 50 325 20 330 0 Z" fill="url(#frontCornerBlob)"/>
    <path class="blob blob--base" d="M0 700 C60 670 120 720 200 705 C280 690 330 640 420 660 C470 670 490 700 507 700 V936 H0 Z" fill="url(#frontBase)"/>
    <rect class="band band--base" y="880" width="507" height="56" fill="var(--magenta)"/>

    <rect class="machine-window-frame" x="34" y="44" width="342" height="610" fill="#55555a"/>
    <rect class="machine-window" x="40" y="50" width="330" height="598" fill="url(#productWindow)" role="img" aria-label="Sichtfenster mit Spiralfächern voller Snacks, Schokoriegel und Getränkeflaschen"/>

    <rect class="instruction-sign" x="424" y="46" width="62" height="70" fill="var(--machine-black)"/>
    <text class="sign-text" x="455" y="60" font-size="7" text-anchor="middle">Bedienung</text>
    <text class="sign-text" x="455" y="76" font-size="6" text-anchor="middle">Münze einwerfen</text>
    <text class="sign-text" x="455" y="88" font-size="6" text-anchor="middle">Nummer wählen</text>
    <text class="sign-text" x="455" y="100" font-size="6" text-anchor="middle">Ware entnehmen</text>

    <rect class="display" x="418" y="210" width="74" height="32" fill="var(--machine-black)"/>
    <rect class="display-screen" x="424" y="218" width="62" height="14" fill="#1f3a44"/>
    <rect class="payment-unit" x="418" y="246" width="74" height="150" fill="var(--machine-black)"/>
    <rect class="coin-slot" x="452" y="255" width="34" height="48" rx="3" fill="#9a9a9e"/>
    <circle class="coin-return" cx="434" cy="290" r="5" fill="#8a8a8e"/>
    <rect class="keypad" x="436" y="335" width="34" height="44" rx="2" fill="#d8d8dc"/>
    <rect class="service-slot" x="416" y="543" width="30" height="116" fill="var(--machine-black)"/>

    <rect class="push-flap" x="95" y="713" width="215" height="79" fill="var(--machine-black)"/>
    <rect class="push-flap-inner" x="105" y="722" width="195" height="61" fill="none" stroke="#2e2e33" stroke-width="2"/>
    <text class="push-label" x="202" y="764" text-anchor="middle">PUSH</text>

    <text class="brand-name brand-name--on-magenta" x="128" y="880" font-size="74" text-anchor="middle">Tulvo's</text>
    <text class="tagline" x="378" y="870" font-size="27" text-anchor="middle" style="stroke-width:3px">Snacks, Getränke</text>
    <text class="tagline" x="382" y="896" font-size="27" text-anchor="middle" style="stroke-width:3px">und Vapes</text>
  </svg>

  <!-- Side wall, right -->
  <svg class="panel panel--right" viewBox="0 0 503 945" preserveAspectRatio="none">
    <defs>
      <linearGradient id="sideTopBlobR" x1="0" y1="0" x2="1" y2="1">
        <stop offset="0" stop-color="#e0338a"/>
        <stop offset="1" stop-color="#f08cbc"/>
      </linearGradient>
      <linearGradient id="sideCornerBlobR" x1="0" y1="0" x2="1" y2="1">
        <stop offset="0" stop-color="#a6417f"/>
        <stop offset="1" stop-color="#d8a6c8"/>
      </linearGradient>
      <linearGradient id="sideCenterBlobR" x1="0" y1="0" x2="0" y2="1">
        <stop offset="0" stop-color="#e86aa8"/>
        <stop offset="1" stop-color="#dd2e87"/>
      </linearGradient>
      <linearGradient id="productArtR" x1="0" y1="0" x2="1" y2="1">
        <stop offset="0" stop-color="#f3b2d0"/>
        <stop offset="1" stop-color="#e985b6"/>
      </linearGradient>
    </defs>
    <rect class="panel-bg" width="503" height="945" fill="var(--blush)"/>
    <path class="blob blob--corner" d="M0 0 H200 C210 40 200 90 170 120 C130 160 60 170 0 150 Z" fill="url(#sideCornerBlobR)"/>
    <path class="blob blob--top" d="M250 0 H503 V185 C470 190 420 200 380 180 C320 150 300 110 270 80 C250 50 240 20 250 0 Z" fill="url(#sideTopBlobR)"/>
    <path class="blob blob--tagline" d="M40 340 C70 300 160 320 230 325 C320 330 360 300 420 320 C480 340 490 420 470 470 C450 520 400 500 340 505 C310 508 320 535 290 535 C260 535 260 505 220 505 C150 505 60 510 35 450 C20 410 25 370 40 340 Z" fill="url(#sideCenterBlobR)"/>
    <path class="band band--floor" d="M0 720 C60 700 120 730 200 745 C300 762 380 720 503 725 V890 H0 Z" fill="var(--plum)"/>
    <rect class="band band--base" y="888" width="503" height="57" fill="var(--magenta)"/>
    <text class="brand-name" x="250" y="300" font-size="128" text-anchor="middle">Tulvo's</text>
    <text class="tagline" x="262" y="405" font-size="46" text-anchor="middle">Snacks, Getränke</text>
    <text class="tagline" x="272" y="452" font-size="46" text-anchor="middle">und Vapes</text>
    <rect class="product-illustration" x="70" y="555" width="340" height="325" rx="22" fill="url(#productArtR)" role="img" aria-label="Illustration: Getränkeflaschen, Chipstüte, Dose, Cracker, Energieriegel, Milchpackung und Keks in Pinktönen"/>
  </svg>

  <!-- Dimension lines -->
  <svg class="dimension" style="left:0;top:0;width:1200px;height:1200px" viewBox="0 0 1200 1200">
    <g stroke="var(--dim-grey)" stroke-width="3" fill="none">
      <line x1="96" y1="271" x2="96" y2="861"/>
      <line x1="87" y1="271" x2="105" y2="271"/>
      <line x1="87" y1="861" x2="105" y2="861"/>

      <line x1="130" y1="889" x2="440" y2="889"/>
      <line x1="130" y1="880" x2="130" y2="898"/>
      <line x1="440" y1="880" x2="440" y2="898"/>

      <line x1="475" y1="889" x2="790" y2="889"/>
      <line x1="475" y1="880" x2="475" y2="898"/>
      <line x1="790" y1="880" x2="790" y2="898"/>

      <line x1="825" y1="889" x2="1135" y2="889"/>
      <line x1="825" y1="880" x2="825" y2="898"/>
      <line x1="1135" y1="880" x2="1135" y2="898"/>
    </g>
  </svg>
  <div class="dimension-label dimension-label--height">1900 mm</div>
  <div class="dimension-label dimension-label--left">1010 mm</div>
  <div class="dimension-label dimension-label--front">1030 mm</div>
  <div class="dimension-label dimension-label--right">1010 mm</div>

</main>
</body>
</html>
```